Mabikay spice shop needs a web design

We need a web design former new company based in sydney australia. Called 'Mabikay, spice shop'.
We produce caribbean/west indies product alcohol, spirits, condiments, candies, preserved food, jams, pates.
We would like to see a design that reflect the caribbean without being tacky.
We want modern, high level design as we do high level products.
Updates

Reason: There is a lot of good proposition but I need a few more days to mature my decision. Thanks for your hard work Jorel

Industry/Entity Type

Hospitality

Number of Pages Required

1 page

Font styles to use
Decorative
Script

Requirements
Must have
• The logo, the name of the business

```html
<!DOCTYPE html>
<html lang="en">
<head>
<meta charset="utf-8">
<title>Mabikay spice shop</title>
<link rel="stylesheet" href="https://fonts.googleapis.com/css2?family=Playball&family=Arimo:ital@0;1&display=swap">
<style>
:root{
  --navy:#24306a;
  --navy-panel:#2b3a78;
  --gold:#c9a42f;
  --gold-soft:#d9c07a;
  --grey:#efefef;
  --white:#ffffff;
  --text:#444444;
  --muted:#777777;
}
*{box-sizing:border-box;margin:0;padding:0}
html,body{width:762px;height:1200px;overflow:hidden;background:var(--white)}
body{position:relative;font-family:"Arimo",Arial,sans-serif;color:var(--text)}
.script{font-family:"Playball",cursive}
.abs{position:absolute}

/* header */
.brand{left:104px;top:10px;width:100px;height:100px;border:1.5px solid var(--gold);border-radius:50%;display:flex;flex-direction:column;align-items:center;justify-content:center;color:var(--navy);font-family:"Playball",cursive;text-align:center;line-height:1}
.brand .name{font-size:26px}
.brand .sub{font-size:11px;margin-top:4px}
.contact{right:104px;top:29px;font-family:"Playball",cursive;font-size:12px;color:var(--gold);white-space:nowrap}
.contact b{font-weight:400;color:var(--navy);font-size:13px}
.contact .sep{color:#ccc;margin:0 8px}
.nav{right:104px;top:64px;display:flex;font-family:"Playball",cursive;font-size:10.5px;color:var(--navy)}
.nav span{margin-left:0}
.nav .sep{color:#ccc;margin:0 10px}
.nav .active{text-decoration:underline}

/* hero */
.hero-photo{left:0;top:121px;width:454px;height:302px;background:radial-gradient(ellipse at 40% 20%,#e0a52a 0%,#8a4d12 45%,#2a1708 100%)}
.hero-panel{left:454px;top:121px;width:308px;height:302px;background:var(--navy-panel)}
.hero-title{left:490px;top:191px;font-family:"Playball",cursive;font-size:31px;line-height:40px;color:var(--white);width:260px}
.hero-title em{font-style:normal;color:var(--gold)}
.dots{left:404px;top:402px;display:flex;gap:3px}
.dots i{width:10px;height:10px;border-radius:50%;background:var(--white)}
.dots i.on{background:var(--gold)}

/* about */
.about{left:0;top:423px;width:762px;height:182px;background:var(--grey)}
.section-title{width:762px;left:0;text-align:center;font-family:"Playball",cursive;font-size:18px;color:var(--navy)}
.about-text{left:210px;top:504px;width:344px;font-size:7.4px;line-height:11.5px;font-style:italic;color:var(--text)}

/* products */
.tabs{left:191px;top:692px;display:flex;gap:3px}
.tab{height:21px;padding:0 6px;background:var(--gold);color:var(--white);font-family:"Playball",cursive;font-size:11px;line-height:21px}
.tab.on{background:var(--navy)}
.card{top:739px;width:96px;height:151px;border:1px solid var(--gold-soft);background:var(--white)}
.bottle{position:absolute;left:34px;top:14px;width:28px;height:124px;border-radius:6px 6px 4px 4px}
.label{top:906px;width:96px;text-align:center;font-family:"Playball",cursive;font-size:11px;color:var(--navy)}
.view-all{left:278px;top:955px;width:205px;display:flex;align-items:center;gap:10px;font-size:7.5px;font-style:italic;color:#333}
.view-all .rule{flex:1;height:1px;background:var(--gold-soft)}

/* band */
.band{left:0;top:1002px;width:762px;height:100px;background:var(--gold)}
.band-title{font-family:"Playball",cursive;font-size:15px;color:var(--white)}
.email-field{left:103px;top:1051px;width:217px;height:26px;border:1px solid var(--gold-soft);font-size:7px;font-style:italic;color:#f3e6bd;padding:9px 8px}
.signup{left:320px;top:1051px;width:57px;height:26px;background:var(--white);color:var(--navy);font-family:"Playball",cursive;font-size:11px;text-align:center;line-height:26px}
.divider{left:441px;top:1018px;width:1px;height:70px;background:#b8952a}
.socials{left:497px;top:1053px;display:flex;gap:6px}
.social{width:28px;height:18px;font-family:"Playball",cursive;font-size:8px;color:var(--white);line-height:18px;text-align:center}

/* footer */
.footer{left:0;top:1102px;width:762px;height:98px;background:var(--grey)}
.footer-links{left:0;top:1121px;width:762px;text-align:center;font-size:7px;font-style:italic;color:var(--text)}
.footer-links .on{color:var(--navy)}
.footer-links .sep{color:var(--gold);margin:0 5px}
.footer-name{left:0;top:1149px;width:762px;text-align:center;font-family:"Playball",cursive;font-size:13px;color:var(--navy)}
.copyright{left:0;top:1179px;width:762px;text-align:center;font-size:7px;font-style:italic;color:var(--muted)}
</style>
</head>
<body>

<header>
  <div class="abs brand"><span class="name">Mabikay</span><span class="sub">spice shop</span></div>
  <div class="abs contact">Call Us : <b>555 014 782</b><span class="sep">/</span>Email Us: <b>hello@mabikayshop.au</b></div>
  <nav class="abs nav">
    <span class="active">Home</span><span class="sep">/</span>
    <span>History</span><span class="sep">/</span>
    <span>Products</span><span class="sep">/</span>
    <span>Wholesale &amp; Special Events</span><span class="sep">/</span>
    <span>News</span><span class="sep">/</span>
    <span>Contact</span>
  </nav>
</header>

<section>
  <div class="abs hero-photo" role="img" aria-label="Wine bottles, filled glasses, grapes and an oak barrel in warm light"></div>
  <div class="abs hero-panel"></div>
  <h1 class="abs hero-title" style="font-weight:400">Now The Best Caribbean <em>Creole Shop</em> In <em>Sydney</em>, Australia</h1>
  <div class="abs dots"><i class="on"></i><i></i><i></i></div>
</section>

<section>
  <div class="abs about"></div>
  <h2 class="abs section-title" style="top:464px;font-weight:400">About Us</h2>
  <p class="abs about-text">Lorem ipsum dolor sit amet, consectetur adipiscing elit, sed do eiusmod tempor incididunt ut labore et dolore magna aliqua. Ut enim ad minim veniam, quis nostrud exercitation ullamco laboris nisi ut aliquip ex ea commodo consequat. Duis aute irure dolor in reprehenderit in voluptate velit esse cillum dolore eu fugiat nulla pariatur. Excepteur sint occaecat cupidatat non proident, sunt in culpa qui officia deserunt mollit anim id est laborum.</p>
</section>

<section>
  <h2 class="abs section-title" style="top:644px;font-weight:400">Our Products</h2>
  <div class="abs tabs">
    <span class="tab on">Alcohol</span><span class="tab">Spirits</span><span class="tab">Condiments</span><span class="tab">Candies</span><span class="tab">Preserved Food</span><span class="tab">Jams</span><span class="tab">Pates</span>
  </div>

  <div class="abs card" style="left:103px"><div class="bottle" role="img" aria-label="Bottle of pink champagne" style="background:linear-gradient(#2a2a2a 0 30%,#e89a9a 30%)"></div></div>
  <div class="abs card" style="left:218px"><div class="bottle" role="img" aria-label="Bottle of dry white wine" style="background:linear-gradient(#222 0 20%,#dfe6b8 20%)"></div></div>
  <div class="abs card" style="left:333px"><div class="bottle" role="img" aria-label="Bottle of semi-dry rosé wine" style="background:linear-gradient(#c9b79a 0 20%,#f0b98a 20% 60%,#d3cdb8 60%)"></div></div>
  <div class="abs card" style="left:448px"><div class="bottle" role="img" aria-label="Bottle of dessert red wine" style="background:linear-gradient(#b0222a 0 15%,#1b1b24 15%)"></div></div>
  <div class="abs card" style="left:563px"><div class="bottle" role="img" aria-label="Bottle of strong white wine" style="background:linear-gradient(#222 0 20%,#e3e7c4 20%)"></div></div>

  <div class="abs label" style="left:103px">Champagne</div>
  <div class="abs label" style="left:218px">Dry Wine</div>
  <div class="abs label" style="left:333px">Semi-Dry Wine</div>
  <div class="abs label" style="left:448px">Dessert Wine</div>
  <div class="abs label" style="left:563px">Strong Wine</div>

  <div class="abs view-all"><span class="rule"></span>view all ...<span class="rule"></span></div>
</section>

<section>
  <div class="abs band"></div>
  <h3 class="abs band-title" style="left:103px;top:1016px;font-weight:400">Newsletter Signup</h3>
  <div class="abs email-field">Enter your email ...</div>
  <div class="abs signup">Signup</div>
  <div class="abs divider"></div>
  <h3 class="abs band-title" style="left:497px;top:1016px;font-weight:400">Follow Us</h3>
  <div class="abs socials">
    <span class="social">Friendbook</span><span class="social">Circlespace</span><span class="social">Chirper</span><span class="social">Snapframe</span>
  </div>
</section>

<footer>
  <div class="abs footer"></div>
  <div class="abs footer-links">
    <span class="on">About Us</span><span class="sep">/</span>Delivery Information<span class="sep">/</span>Privacy Policy<span class="sep">/</span>Terms &amp; Conditions<span class="sep">/</span>Customer Service<span class="sep">/</span>Contact Us<span class="sep">/</span>Returns<span class="sep">/</span>Site Map
  </div>
  <div class="abs footer-name">Mabikay</div>
  <div class="abs copyright">Mabikay, spice shop © 2015 All Rights Reserved</div>
</footer>

</body>
</html>
```